Pull-Up Banner for creating escape room themed engaging learning experiences

Our research group create engaging learning experiences aimed at the following markets: Primary school, secondary school, tertiary and corporate training. We want learning to be fun, but also deep - where participants will need to think deeply and apply themselves to solve problems as a team.
We are the inventors of the open source escape room decoder box and want to engage students in learning in a fun way which maximizes teamwork. We are also keen to be contracted to design custom escape room learning experiences for corporate entities to engage their staff and have them working together as a team.

```html
<!DOCTYPE html>
<html lang="en">
<head>
<meta charset="utf-8">
<title>Puzzle Quest Learning – Pull-Up Banner</title>
<link href="https://fonts.googleapis.com/css2?family=Montserrat:wght@500;600;700&display=swap" rel="stylesheet">
<style>
  :root {
    --page-bg: #f1f1f1;
    --banner-white: #ffffff;
    --stripe-grey: #ececec;
    --ink-dark: #4a4a4a;
    --ink-black: #111111;
    --band-black: #000000;
    --brand-orange: #f28a1c;
  }
  html, body {
    margin: 0;
    padding: 0;
    width: 789px;
    height: 1200px;
    overflow: hidden;
    background: var(--page-bg);
    font-family: "Montserrat", Arial, sans-serif;
  }
  .banner {
    position: absolute;
    left: 154px;
    top: 50px;
    width: 480px;
    height: 1100px;
    background: var(--banner-white);
    box-shadow: 0 4px 18px rgba(0,0,0,0.18);
    overflow: hidden;
  }
  .banner-graphics {
    position: absolute;
    inset: 0;
  }
  .brand {
    position: absolute;
    top: 78px;
    left: 0;
    width: 480px;
    display: flex;
    align-items: center;
    justify-content: center;
    gap: 12px;
  }
  .brand-dot {
    width: 34px;
    height: 34px;
    border-radius: 50%;
    background: var(--brand-orange);
  }
  .brand-name {
    font-weight: 700;
    font-size: 27px;
    color: var(--brand-orange);
    letter-spacing: -0.3px;
    text-transform: uppercase;
  }
  .headline {
    position: absolute;
    top: 165px;
    left: 0;
    width: 480px;
    margin: 0;
    text-align: center;
    font-weight: 600;
    font-size: 31px;
    line-height: 39.5px;
    color: var(--ink-dark);
    text-transform: uppercase;
    letter-spacing: -0.4px;
  }
  .web-address {
    position: absolute;
    top: 1043px;
    left: 0;
    width: 480px;
    text-align: center;
    font-weight: 600;
    font-size: 22px;
    color: var(--ink-black);
    letter-spacing: 0.2px;
  }
  .web-address .web-name { color: var(--brand-orange); }
</style>
</head>
<body>
  <div class="banner">
    <svg class="banner-graphics" width="480" height="1100" viewBox="0 0 480 1100">
      <defs>
        <!-- team around a table: dark window top left, warm skin middle, light table bottom -->
        <radialGradient id="photoTeam" cx="0.5" cy="0.55" r="0.7">
          <stop offset="0" stop-color="#c9a48c"/>
          <stop offset="0.35" stop-color="#b7aea2"/>
          <stop offset="0.65" stop-color="#6d6f70"/>
          <stop offset="1" stop-color="#2f3a42"/>
        </radialGradient>
        <linearGradient id="photoTeamFloor" x1="0" y1="0" x2="0" y2="1">
          <stop offset="0" stop-color="#ffffff" stop-opacity="0"/>
          <stop offset="0.75" stop-color="#ffffff" stop-opacity="0"/>
          <stop offset="1" stop-color="#f1eee8" stop-opacity="0.85"/>
        </linearGradient>
        <!-- bright meeting room -->
        <linearGradient id="photoMeeting" x1="0" y1="0" x2="0" y2="1">
          <stop offset="0" stop-color="#e6e6e6"/>
          <stop offset="0.5" stop-color="#a59a90"/>
          <stop offset="0.8" stop-color="#e9dcc4"/>
          <stop offset="1" stop-color="#bdb8ae"/>
        </linearGradient>
        <!-- decoder box group with red sign -->
        <linearGradient id="photoDecoderGroup" x1="0" y1="0" x2="1" y2="1">
          <stop offset="0" stop-color="#d8d8d8"/>
          <stop offset="0.45" stop-color="#b98276"/>
          <stop offset="0.7" stop-color="#7a7f8a"/>
          <stop offset="1" stop-color="#e4e1dc"/>
        </linearGradient>
        <!-- dark room with red laser and yellow top -->
        <linearGradient id="photoLaser" x1="0" y1="0" x2="1" y2="1">
          <stop offset="0" stop-color="#2b2b30"/>
          <stop offset="0.4" stop-color="#8a3232"/>
          <stop offset="0.65" stop-color="#c79a2e"/>
          <stop offset="1" stop-color="#2e3340"/>
        </linearGradient>
        <!-- keypad decoder in hand -->
        <radialGradient id="photoKeypad" cx="0.5" cy="0.45" r="0.6">
          <stop offset="0" stop-color="#8f93a8"/>
          <stop offset="0.35" stop-color="#6a6668"/>
          <stop offset="0.7" stop-color="#3b2f2a"/>
          <stop offset="1" stop-color="#1c1a1a"/>
        </radialGradient>
      </defs>

      <g class="background-stripes" fill="var(--stripe-grey)" opacity="0.7">
        <polygon points="480,0 480,120 300,0"/>
        <polygon points="480,150 480,330 130,0 250,0"/>
        <polygon points="0,300 0,440 200,640 280,640"/>
        <polygon points="0,520 0,600 90,680 170,680"/>
      </g>

      <polygon class="black-panel" points="0,684 480,477 480,1021 0,1021" fill="var(--band-black)"/>

      <g class="feature-photo">
        <path d="M 230 377 A 220 220 0 0 0 60 780" fill="none" stroke="var(--brand-orange)" stroke-width="2"/>
        <path d="M 415 460 A 220 220 0 0 1 240 818" fill="none" stroke="var(--brand-orange)" stroke-width="2"/>
        <circle cx="238" cy="594" r="202" fill="url(#photoTeam)" role="img" aria-label="Photo: three adults leaning over a table, solving an escape room puzzle together"/>
        <circle cx="238" cy="594" r="202" fill="url(#photoTeamFloor)"/>
      </g>

      <g class="inset-photo">
        <circle cx="324" cy="416" r="85" fill="none" stroke="var(--brand-orange)" stroke-width="2"/>
        <circle cx="324" cy="416" r="77" fill="url(#photoMeeting)" stroke="#fff" stroke-width="3" role="img" aria-label="Photo: facilitator guiding a team working on clues at a meeting table"/>
      </g>

      <g class="thumb-row">
        <path d="M 104 815 A 66 66 0 0 1 104 947" fill="none" stroke="var(--brand-orange)" stroke-width="2"/>
        <path d="M 104 947 A 66 66 0 0 1 44 912" fill="none" stroke="var(--brand-orange)" stroke-width="2"/>
        <circle cx="104" cy="881" r="60" fill="url(#photoDecoderGroup)" role="img" aria-label="Photo: team gathered around a decoder box in a STEM room"/>
        <path d="M 245 815 A 66 66 0 0 1 245 947" fill="none" stroke="var(--brand-orange)" stroke-width="2"/>
        <path d="M 245 947 A 66 66 0 0 1 185 912" fill="none" stroke="var(--brand-orange)" stroke-width="2"/>
        <circle cx="245" cy="881" r="60" fill="url(#photoLaser)" role="img" aria-label="Photo: students in a dark room working past red laser beams"/>
        <path d="M 384 815 A 66 66 0 0 1 384 947" fill="none" stroke="var(--brand-orange)" stroke-width="2"/>
        <path d="M 384 947 A 66 66 0 0 1 324 912" fill="none" stroke="var(--brand-orange)" stroke-width="2"/>
        <circle cx="384" cy="881" r="60" fill="url(#photoKeypad)" role="img" aria-label="Photo: hand holding an electronic keypad decoder with a laser"/>
      </g>
    </svg>

    <div class="brand">
      <span class="brand-dot"></span>
      <span class="brand-name">Puzzle Quest Learning</span>
    </div>

    <h1 class="headline">Primary school,<br>secondary school,<br>tertiary and<br>corporate training</h1>

    <div class="web-address">www.<span class="web-name">puzzlequestlearning</span>.com</div>
  </div>
</body>
</html>
```